Tordo Brand Fuego Cut Jalapeños

Company Background Information:
Tordo Brand Farms is a family owned and operated business since 1981. Our Jalapeños are grown through sustainable practices environmentally socially and economically. We are a company based in Mexico looking to enter the U.S. and international retail market.
Packaging Design Description:
We manufacture Fuego Cut Jalapeño Peppers on a stand up pouch bag with a zipper. We currently are labeling as can be seen in attached picture, but I am looking for a design to be printed in the bag on both sides front and back that will stand out in the shelf of the retail market.
Attached are the photo files of the bag dimensions and the finished product with current label.
Requirements:
1. Logo: Tordo Brand (Attached in file)
2. Name of Product: Fuego Cut Jalapeño Peppers
3. Generic Nutrition Facts panel.
4. " Best Before: " (For expiration date purposes)
5. " Refrigerate after opening"
6. Ingredients: Jalapeño Peppers, Water, Vinegar, Salt, Oregano, Bay Leaf, Garlic, Thyme & Calcium Chloride
7. Net Wt. 16 oz
8. Generic Bar Code
9. Processed by: Empacadora Cerro Azufre S.A. de C.V.
Av. Quintero 482 Int. 3 Col. Centro
Guaymas, Son. Mexico
10. www.tordobrand.example
11. e-mail info@tordobrand.example
12. Phone: 52(987)654-3210
We would like a fresh appearance. Somewhat traditional. It is also directed towards a more economical market.
Target Market(s)
Our target market is mostly the latino population in the United States, the growing diversity of cultures in the US is helping people try different cuisines, spicy foods in our case.

```html
<!DOCTYPE html>
<html lang="en">
<head>
<meta charset="utf-8">
<title>Tordo Brand Fuego Cut Jalapeño Peppers – Pouch Artwork</title>
<link rel="stylesheet" href="https://fonts.googleapis.com/css2?family=Barlow+Condensed:wght@400;500;600;700&family=Barlow:wght@400;600&display=swap">
<style>
  :root {
    --bg: #e4e4e4;
    --pouch-red: #c8141c;
    --pouch-red-deep: #8e0b10;
    --flame-orange: #f0742a;
    --flame-yellow: #ffc23a;
    --band-gold: #e8961c;
    --band-maroon: #8a1a12;
    --cream: #ffe7a8;
    --white: #ffffff;
    --ink: #1f1f1f;
    --pepper-green: #2f9a2c;
    --pepper-light: #7cc953;
  }
  * { box-sizing: border-box; margin: 0; padding: 0; }
  html, body { width: 1200px; height: 960px; overflow: hidden; }
  body {
    background: var(--bg);
    font-family: "Barlow Condensed", "Arial Narrow", sans-serif;
    position: relative;
  }
  .pouch {
    position: absolute;
    top: 140px;
    width: 500px;
    height: 680px;
    background: radial-gradient(ellipse at 50% 45%, var(--pouch-red) 0%, var(--pouch-red) 55%, var(--pouch-red-deep) 100%);
    overflow: hidden;
    color: var(--white);
  }
  .pouch--front { left: 70px; }
  .pouch--back { left: 630px; background: linear-gradient(180deg, var(--pouch-red) 0%, #b5111a 100%); }

  .side-band {
    position: absolute;
    top: 0; bottom: 0;
    width: 34px;
    background: linear-gradient(90deg, var(--band-gold) 0%, #c9661a 50%, var(--band-gold) 100%);
  }
  .side-band--left { left: 0; }
  .side-band--right { right: 0; }

  .flames {
    position: absolute;
    left: 34px; right: 34px; top: 0; bottom: 0;
    background:
      radial-gradient(ellipse 30% 45% at 18% 30%, rgba(255,150,40,.55), transparent 70%),
      radial-gradient(ellipse 28% 40% at 85% 25%, rgba(255,170,50,.5), transparent 70%),
      radial-gradient(ellipse 60% 35% at 50% 80%, rgba(255,140,30,.55), transparent 70%);
  }

  .tear-line {
    position: absolute;
    left: 34px; right: 34px; top: 92px;
    border-top: 1px solid rgba(0,0,0,.25);
  }
  .tear-hint {
    position: absolute;
    right: 58px; top: 52px;
    font-size: 20px; font-weight: 500;
    color: var(--cream);
    letter-spacing: .5px;
    display: flex; align-items: center; gap: 10px;
  }

  .brand-name {
    position: absolute;
    left: 0; right: 0;
    text-align: center;
    font-weight: 600;
    color: var(--white);
    display: flex; justify-content: center; align-items: center; gap: 12px;
  }
  .brand-name .dot { width: 16px; height: 16px; border-radius: 50%; background: var(--pepper-light); flex: none; }
  .pouch--front .brand-name { top: 160px; font-size: 64px; line-height: 1; }
  .brand-rule {
    position: absolute; left: 150px; right: 150px; top: 258px;
    border-top: 3px solid var(--white);
  }

  .product-title {
    position: absolute;
    left: 34px; right: 34px; top: 300px;
    text-align: center;
    font-weight: 600;
    font-size: 58px;
    line-height: 1.05;
    text-shadow: 0 3px 4px rgba(0,0,0,.4);
  }

  .pepper-photo {
    position: absolute;
    left: 84px; top: 448px; width: 370px; height: 150px;
    border-radius: 70px 60px 50px 80px;
    background: radial-gradient(ellipse at 40% 50%, var(--pepper-light) 0%, var(--pepper-green) 55%, #1d6b1b 100%);
  }

  .net-weight {
    position: absolute;
    left: 0; right: 0; top: 608px;
    text-align: center; font-weight: 600;
    line-height: 1.05;
  }
  .net-weight .label { font-size: 24px; display: block; }
  .net-weight .value { font-size: 32px; display: block; }

  /* back */
  .zip-hint {
    position: absolute; left: 60px; top: 44px;
    font-size: 19px; font-weight: 500; color: var(--cream);
    display: flex; align-items: center; gap: 8px;
  }
  .back-header { position: absolute; left: 60px; top: 112px; right: 50px; display: flex; align-items: center; gap: 26px; }
  .back-header .brand-name { position: static; font-size: 36px; }
  .back-title { font-size: 25px; font-weight: 700; color: var(--cream); line-height: 1.05; }
  .ingredients {
    position: absolute; left: 60px; right: 50px; top: 196px;
    font-family: "Barlow", Arial, sans-serif; font-size: 13px; line-height: 1.6;
    color: var(--flame-yellow); text-align: center;
  }
  .storage {
    position: absolute; left: 60px; right: 50px; top: 254px;
    font-size: 26px; font-weight: 400; letter-spacing: .5px; text-align: center;
    border-bottom: 1px solid rgba(255,255,255,.7); padding-bottom: 6px;
  }
  .nutrition {
    position: absolute; left: 60px; top: 318px; width: 160px;
    background: var(--white); color: var(--ink);
    border: 2px solid var(--ink);
    font-family: "Barlow", Arial, sans-serif; font-size: 9px;
    padding: 4px 5px;
  }
  .nutrition h3 { font-family: "Barlow Condensed", sans-serif; font-size: 14px; text-align: center; border-bottom: 1px solid var(--ink); }
  .nutrition .serving { text-align: center; line-height: 1.3; border-bottom: 3px solid var(--ink); padding: 2px 0; }
  .nutrition table { width: 100%; border-collapse: collapse; }
  .nutrition td { border-bottom: 1px solid #999; padding: 1px 0; }
  .nutrition td:last-child { text-align: right; }
  .nutrition .indent { padding-left: 12px; }
  .processor {
    position: absolute; left: 236px; top: 322px; width: 220px;
    font-family: "Barlow", Arial, sans-serif; font-size: 10.5px; line-height: 1.45;
    color: var(--cream); font-style: normal;
  }
  .back-net { position: absolute; left: 236px; top: 440px; font-size: 20px; font-weight: 600; }
  .back-rule { position: absolute; left: 60px; right: 50px; top: 480px; border-top: 1px solid rgba(255,255,255,.6); }
  .lot-box {
    position: absolute; left: 60px; top: 500px; width: 130px; height: 48px;
    background: var(--white); color: var(--ink);
    font-family: "Barlow", Arial, sans-serif; font-size: 10px; line-height: 1.5; padding: 5px 8px;
  }
  .barcode-area {
    position: absolute; left: 206px; top: 520px; width: 244px; height: 70px;
    background: var(--white);
  }
  .badges { position: absolute; left: 62px; top: 562px; display: flex; gap: 12px; }
  .badges span { width: 18px; height: 18px; border-radius: 50%; background: var(--white); opacity: .9; }
</style>
</head>
<body>

<section class="pouch pouch--front" aria-label="Pouch front">
  <div class="flames" role="img" aria-label="Flame illustration across the red background"></div>
  <div class="side-band side-band--left" role="img" aria-label="Traditional geometric border pattern in gold and maroon"></div>
  <div class="side-band side-band--right" role="img" aria-label="Traditional geometric border pattern in gold and maroon"></div>

  <div class="tear-line"></div>
  <p class="tear-hint">TEAR HERE TO OPEN
    <svg width="10" height="14" viewBox="0 0 10 14"><path d="M0 0 L10 7 L0 14 Z" fill="#ffe7a8"/></svg>
  </p>

  <p class="brand-name"><span class="dot"></span>Tordo Brand</p>
  <div class="brand-rule"></div>

  <h1 class="product-title">FUEGO CUT<br>JALAPEÑO PEPPERS</h1>

  <div class="pepper-photo" role="img" aria-label="Photo of sliced green jalapeño rings"></div>

  <p class="net-weight"><span class="label">NET WT.</span><span class="value">16 OZ</span></p>
</section>

<section class="pouch pouch--back" aria-label="Pouch back">
  <div class="side-band side-band--left" role="img" aria-label="Traditional geometric border pattern in gold and maroon"></div>
  <div class="side-band side-band--right" role="img" aria-label="Traditional geometric border pattern in gold and maroon"></div>

  <p class="zip-hint">
    <svg width="14" height="12" viewBox="0 0 14 12"><path d="M13 11 C13 5 8 3 3 3 M3 3 L6 0 M3 3 L6 6" stroke="#ffe7a8" stroke-width="2" fill="none"/></svg>
    OPEN-CLOSE ZIPLOCK TO KEEP'EM FRESH!
  </p>

  <div class="back-header">
    <p class="brand-name"><span class="dot"></span>Tordo Brand</p>
    <h2 class="back-title">FUEGO CUT<br>JALAPEÑO PEPPERS</h2>
  </div>

  <p class="ingredients">Ingredients: Jalapeño Peppers, Water, Vinegar, Salt,<br>Oregano, Bay Leaf, Garlic, Thyme &amp; Calcium Chloride</p>

  <p class="storage">REFRIGERATE AFTER OPENING</p>

  <div class="nutrition">
    <h3>NUTRITION FACTS</h3>
    <p class="serving">Servings per package: ?<br>Serving size: ?</p>
    <table>
      <tr><td></td><td>Amount / 100ml</td></tr>
      <tr><td>Energy</td><td>40 Kcal</td></tr>
      <tr><td>Carbohydrates</td><td>10.0 g</td></tr>
      <tr><td class="indent">Sugar</td><td>9.5 g</td></tr>
      <tr><td>Protein</td><td>0 g</td></tr>
      <tr><td>Fats</td><td>0 g</td></tr>
      <tr><td>Sodium</td><td>30 mg</td></tr>
    </table>
  </div>

  <address class="processor">
    Processed by:<br>
    Empacadora Cerro Azufre S.A. de C.V.<br>
    Av. Quintero 482 Int. 3 Col. Centro<br>
    Guaymas, Son. Mexico<br>
    Phone: 52(987)654-3210<br>
    www.tordobrand.example<br>
    e-mail info@tordobrand.example
  </address>

  <p class="back-net">NET WT. 16 OZ</p>
  <div class="back-rule"></div>

  <div class="lot-box">LOT NR:<br>BEST BEFORE:</div>

  <div class="barcode-area" role="img" aria-label="Space reserved for the generic product barcode"></div>

  <div class="badges" aria-label="Certification marks">
    <span></span><span></span><span></span><span></span>
  </div>
</section>

</body>
</html>
```